Wexley Foot & Ankle Martinsburg Window Vinyl Cling

Hi,
I'm looking to get a window decal done, but need it professionally designed.
-must be 24" x 24"
-Quorum Font
-Include our logo, Podiatry, phone number and website
- The goal is to make this eye catching.
Thank you,
Dorian

```html
<!DOCTYPE html>
<html lang="en">
<head>
<meta charset="utf-8">
<title>Wexley Foot &amp; Ankle Martinsburg – Podiatry Window Cling</title>
<link rel="stylesheet" href="https://fonts.googleapis.com/css2?family=Caudex:wght@700&family=Montserrat:wght@700&display=swap">
<style>
  :root {
    --teal: #59c2a7;
    --orange: #f2804a;
    --white: #ffffff;
  }
  html, body {
    margin: 0;
    padding: 0;
    width: 1200px;
    height: 1200px;
    overflow: hidden;
    background: var(--white);
  }
  .cling {
    position: relative;
    width: 1200px;
    height: 1200px;
    background: var(--white);
    font-family: "Caudex", Georgia, serif;
    font-weight: 700;
  }
  .headline-band {
    position: absolute;
    left: 0; top: 0;
    width: 1200px;
    height: 324px;
    background: var(--teal);
    display: flex;
    align-items: center;
    justify-content: center;
  }
  .headline {
    margin: 0;
    color: var(--white);
    font-size: 178px;
    line-height: 1;
    letter-spacing: -1px;
    padding-bottom: 14px;
  }
  .line {
    position: absolute;
    left: 0;
    width: 1200px;
    margin: 0;
    text-align: center;
    white-space: nowrap;
    color: var(--orange);
    line-height: 1;
  }
  .tagline {
    top: 354px;
    font-size: 78px;
    letter-spacing: 1px;
  }
  .pill {
    position: absolute;
    left: 514px;
    width: 172px;
    height: 52px;
    border-radius: 16px;
    background: var(--teal);
    color: var(--white);
    font-family: "Montserrat", Arial, sans-serif;
    font-weight: 700;
    font-size: 31px;
    display: flex;
    align-items: center;
    justify-content: center;
    letter-spacing: 0.5px;
  }
  .pill-call { top: 447px; }
  .pill-visit { top: 640px; }
  .phone {
    top: 518px;
    font-size: 112px;
    letter-spacing: 1px;
  }
  .website {
    top: 706px;
    font-size: 78px;
    letter-spacing: 0;
  }
  .divider {
    position: absolute;
    left: 10px;
    top: 830px;
    width: 1180px;
    height: 3px;
    background: var(--teal);
  }
  .brand {
    position: absolute;
    left: 0; top: 860px;
    width: 1200px;
    height: 340px;
  }
  .brand-mark {
    position: absolute;
    left: 40px;
    top: 40px;
    width: 270px;
    height: 270px;
    border-radius: 50%;
    background: var(--teal);
  }
  .brand-name {
    position: absolute;
    right: 12px;
    top: 36px;
    margin: 0;
    color: var(--orange);
    font-size: 100px;
    line-height: 1.04;
    text-align: right;
    white-space: nowrap;
  }
  .brand-name span { display: block; }
  .brand-name .brand-place { font-size: 84px; }
</style>
</head>
<body>
<main class="cling">
  <header class="headline-band">
    <h1 class="headline">Podiatry</h1>
  </header>

  <p class="line tagline">FOOT &amp; ANKLE PHYSICIANS</p>

  <div class="pill pill-call">CALL</div>
  <p class="line phone">(877) 555 0142</p>

  <div class="pill pill-visit">VISIT</div>
  <p class="line website">WEXLEYFEET.COM</p>

  <div class="divider"></div>

  <footer class="brand">
    <div class="brand-mark"></div>
    <h2 class="brand-name">
      <span>WEXLEY</span>
      <span>FOOT &amp; ANKLE</span>
      <span class="brand-place">MARTINSBURG</span>
    </h2>
  </footer>
</main>
</body>
</html>
```